Design a styled business card for an intimacy and attachment psychologist

I am a Psychologist providing online therapy to patients across the United States. My work is interpersonal and emotion-focused, with an emphasis on the client-therapist relationship. My primary areas of work are very personal, including sexuality and gender, abuse and trauma, and grief and loss. My target audience will be adults of all ages 18+.
My business card should convey a warm and inviting feeling of professionalism that is also casual and comfortable.
The front should be fairly simple and professional, consisting of:
- My name, Dr. Rosalind Pembrook
- My title, Licensed Psycholigist
- My logo
On either the front or the back, my contact information should be listed:
- ros@drrospembrook.example
- 555.014.7789
- drrospembrook.example
On the rear, I would like a description of the areas that I specialize in. This can be formatted in any way that appears stylistically interesting.
Individual and Couples
Relationships and Infidelity
Sexual Health & Aging
Gender Identity & Sexual Orientation
Abuse and Trauma
Sexual Compulsivity & Addiction
Sexual Dysfunction
Target Market(s)
My target audience will be adults of all ages 18+.
Industry/Entity Type
Psychology
Contact Information for Business Card
The front should be fairly simple and professional, consisting of: - My name, Dr. Rosalind Pembrook - My title, Licensed Psycholigist - My logo On either the front or the back, my contact information should be listed: - ros@drrospembrook.example - 555.014.7789 - drrospembrook.example On the rear, I would like a description of the areas that I specialize in. This can be formatted in any way that appears stylistically interesting. Individual and Couples Relationships and Infidelity Sexual Health & Aging Gender Identity & Sexual Orientation Abuse and Trauma Sexual Compulsivity & Addiction Sexual Dysfunction

```html
<!DOCTYPE html>
<html lang="en">
<head>
<meta charset="utf-8">
<title>Dr. Rosalind Pembrook – Business Card</title>
<link rel="stylesheet" href="https://fonts.googleapis.com/css2?family=Cinzel:wght@500&family=Poppins:wght@400&display=swap">
<style>
  :root {
    --navy: #2b2550;
    --teal: #4dd4b4;
    --mint: #c9f1e6;
    --purple: #9b4fbf;
    --white: #ffffff;
    --page: #e9e6ef;
    --serif: "Cinzel", "Times New Roman", serif;
    --sans: "Poppins", Arial, sans-serif;
  }
  * { box-sizing: border-box; margin: 0; padding: 0; }
  html, body { width: 1200px; height: 900px; overflow: hidden; }
  body { background: var(--page); position: relative; font-family: var(--sans); }

  .card {
    position: absolute;
    width: 640px;
    height: 366px;
    overflow: hidden;
    box-shadow: 0 10px 24px rgba(30, 24, 60, 0.25);
  }

  /* Back: specialties */
  .card-back { left: 70px; top: 60px; background: var(--navy); color: var(--white); }
  .card-back .brand {
    position: absolute; left: 110px; top: 62px;
    display: flex; align-items: center; gap: 30px;
  }
  .brand-dot {
    width: 118px; height: 118px; border-radius: 50%;
    background: var(--teal); flex: none;
  }
  .brand-name {
    font-family: var(--serif); font-weight: 500;
    line-height: 0.95; text-transform: uppercase;
  }
  .card-back .brand-name { font-size: 40px; color: var(--white); }
  .brand-name .title-prefix { display: block; font-size: 0.55em; padding-left: 4px; }
  .specialties {
    position: absolute; left: 0; right: 0; top: 232px;
    list-style: none; text-align: center;
    font-size: 15px; line-height: 1.45; letter-spacing: 0.2px;
  }

  /* Front: contact */
  .card-front { left: 490px; top: 474px; background: var(--white); color: var(--navy); }
  .identity { position: absolute; left: 50px; top: 48px; }
  .identity .person {
    font-family: var(--serif); font-weight: 500; font-size: 21px;
    text-transform: uppercase; letter-spacing: 0.5px;
  }
  .identity .role { font-size: 16px; margin-top: 2px; }
  .card-front .brand {
    position: absolute; right: 40px; top: 30px;
    display: flex; flex-direction: column; align-items: center; gap: 14px;
  }
  .card-front .brand-dot { width: 82px; height: 82px; }
  .card-front .brand-name { font-size: 30px; color: var(--navy); }
  .contacts {
    position: absolute; left: 62px; top: 196px;
    list-style: none; font-size: 16px; line-height: 1.55;
  }
  .contacts li { display: flex; align-items: center; gap: 10px; }
  .contacts svg { width: 16px; height: 16px; flex: none; }
  .wave { position: absolute; left: 0; bottom: 0; width: 640px; height: 150px; }
</style>
</head>
<body>

<section class="card card-back" aria-label="Business card back">
  <div class="brand">
    <div class="brand-dot"></div>
    <div class="brand-name"><span class="title-prefix">Dr.</span>Rosalind<br>Pembrook</div>
  </div>
  <ul class="specialties">
    <li>Individual and Couples | Relationships and Infidelity</li>
    <li>Sexual Health &amp; Aging | Sexual Dysfunction</li>
    <li>Sexual Compulsivity &amp; Addiction | Abuse and Trauma</li>
    <li>Gender Identity &amp; Sexual Orientation</li>
  </ul>
</section>

<section class="card card-front" aria-label="Business card front">
  <div class="identity">
    <p class="person">Dr. Rosalind Pembrook</p>
    <p class="role">Licensed Psycholigist</p>
  </div>

  <div class="brand">
    <div class="brand-dot"></div>
    <div class="brand-name"><span class="title-prefix">Dr.</span>Rosalind<br>Pembrook</div>
  </div>

  <ul class="contacts">
    <li>
      <svg viewBox="0 0 16 16" aria-hidden="true"><path d="M3.5 1.5l2.5 0 1 3.5-1.6 1.2a8 8 0 0 0 4.4 4.4L11 9l3.5 1v2.5c0 1-1 2-2 2A11 11 0 0 1 1.5 3.5c0-1 1-2 2-2z" fill="var(--navy)"/></svg>
      555.014.7789
    </li>
    <li>
      <svg viewBox="0 0 16 16" aria-hidden="true"><rect x="1" y="3" width="14" height="10" fill="var(--navy)"/><path d="M1 3l7 6 7-6" fill="none" stroke="var(--white)" stroke-width="1.2"/></svg>
      ros@drrospembrook.example
    </li>
    <li>
      <svg viewBox="0 0 16 16" aria-hidden="true"><g fill="none" stroke="var(--navy)" stroke-width="1.3"><circle cx="8" cy="8" r="6.5"/><ellipse cx="8" cy="8" rx="3" ry="6.5"/><path d="M1.5 8h13M2.5 4.5h11M2.5 11.5h11"/></g></svg>
      drrospembrook.example
    </li>
  </ul>

  <svg class="wave" viewBox="0 0 640 150" preserveAspectRatio="none" aria-hidden="true">
    <path d="M0 90 C180 118 330 88 450 40 C530 10 590 2 640 0 L640 150 L0 150 Z" fill="var(--teal)"/>
    <path d="M0 104 C190 122 340 90 470 48 C540 24 600 16 640 14 L640 150 L0 150 Z" fill="var(--white)"/>
    <path d="M420 56 C500 22 580 8 640 4 L640 14 C580 18 510 32 450 52 Z" fill="var(--purple)"/>
    <path d="M0 112 C200 126 350 94 480 52 C550 30 605 24 640 22 L640 150 L0 150 Z" fill="var(--navy)"/>
  </svg>
</section>

</body>
</html>
```